Marlow Crest Cellars wine is looking for a modern, bold contemporary abstract logo/brand design

We are wholesale distributor based in Napa Valley / Sonoma county in California, USA which needs an universal logo/brand name design for all our potential products include pouches, lumo kart and Bag in Box package. All products will be export to Asia predominantly in the greater China market we have yet finalize on company name at this moment but leaning toward "Tavin" as our brand name.

With our target group age between 21-45, we would like to see modern designs that is suitable for our target audience which include minimum requirement usage in colors of Red and Gold to reflect the Asian culture with generic grape, vineyard and other wine industry images. As an alternate option, image can also be formed in any musical instrument or even in animal symbols such as cheetah and black panther whatever suitable to the overall design. We want the image of the product to be stand out from other competitor envision the box design as royal, luxury with texture in modern twist.

The final design should communicate environmental safety, wine composition information (bottle wine equivalent volume images, place of origin such as Made in the U.S.A., Napa Valley, Sonoma, California wordings and all other wine industry standard relevant information listed on package).

Attached pictures are for your reference.

Target Market(s)

Age group 21-45, Asia market predominately in the greater China region

Industry/Entity Type

Distributor

Font styles to use
Serif
Decorative
Script

Requirements
Must have
• 1. Modern bold contemporary abstract design - see attached
• 2. Prefer colors in mixture of Gold, Red, Black in Red Wine package, and colors in mixture of Gold, Silver, Copper, Brass, Steel in White Wine package.
• 3. Brand name "Tavin"
Nice to have
• 1. Generic grapes, vineyard, wine industry images and/or non-winery images in musical instrument or animal symbol such as horse in standing figure whatever suitable to the overall design concept.
• 2. Place of origin wordings such as Products of U.S.A., California Red Wine and etc.

```html
<!DOCTYPE html>
<html lang="en">
<head>
<meta charset="utf-8">
<title>Tavin California Red Wine – Carton Dieline</title>
<link rel="stylesheet" href="https://fonts.googleapis.com/css2?family=Russo+One&family=Montserrat:wght@600;700&family=Yellowtail&family=Oswald:wght@500&display=swap">
<style>
  :root {
    --ink: #1b1b1b;
    --paper: #ffffff;
    --wine-red: #d3132a;
    --deep-red: #7a0f16;
    --line: #9a9a9a;
    --stage-top: #ececec;
    --stage-bottom: #bdbdbd;
  }
  * { box-sizing: border-box; margin: 0; padding: 0; }
  html, body { width: 1200px; height: 1000px; overflow: hidden; }
  body {
    position: relative;
    background: linear-gradient(180deg, var(--stage-top), var(--stage-bottom));
    font-family: "Montserrat", sans-serif;
  }
  .dieline-lines { position: absolute; left: 0; top: 0; }
  .panel { position: absolute; background: var(--ink); color: var(--paper); overflow: hidden; }
  .panel--side-a { left: 97px; top: 165px; width: 150px; height: 320px; }
  .panel--front  { left: 247px; top: 165px; width: 250px; height: 320px; }
  .panel--side-b { left: 497px; top: 165px; width: 150px; height: 320px; }
  .panel--back   { left: 647px; top: 165px; width: 250px; height: 320px; }
  .panel__white-half { position: absolute; left: 0; top: 0; width: 128px; height: 100%; background: var(--paper); }

  .brand-name { position: absolute; font-family: "Russo One", sans-serif; color: var(--wine-red); line-height: 1; letter-spacing: 1px; }
  .tagline { position: absolute; font-family: "Yellowtail", cursive; color: var(--wine-red); line-height: 1; white-space: nowrap; }
  .small-print { position: absolute; font-size: 6.5px; font-weight: 700; text-align: center; line-height: 11px; width: 100%; }
  .volume { position: absolute; font-family: "Oswald", sans-serif; font-weight: 500; line-height: 1; }
  .abv { position: absolute; font-family: "Oswald", sans-serif; font-size: 11px; width: 100%; text-align: center; }

  .origin-tag { position: absolute; left: 0; top: 38px; width: 128px; height: 11px; background: var(--ink);
    clip-path: polygon(0 0, 92% 0, 100% 100%, 0 100%); color: var(--paper);
    font-size: 7px; font-weight: 700; padding-left: 20px; line-height: 11px; }
  .front-brand { left: 15px; top: 57px; font-size: 40px; }
  .front-tagline { left: 18px; top: 97px; font-size: 17px; }
  .art-panther { position: absolute; left: 6px; top: 125px; width: 238px; height: 180px;
    background: radial-gradient(ellipse at 55% 55%, #2a2a2a 0%, #555 45%, rgba(120,120,120,0.15) 75%, transparent 80%); }
  .front-volume { left: 18px; top: 296px; font-size: 14px; color: var(--ink); }

  .side-brand { left: 0; width: 100%; text-align: center; top: 56px; font-size: 21px; }
  .side-tagline { left: 0; width: 100%; text-align: center; top: 88px; font-size: 12px; }
  .map-area { position: absolute; left: 60px; top: 138px; width: 36px; height: 48px; background: linear-gradient(#cfcfcf, #9d9d9d); }
  .glass-outline { position: absolute; left: 0; top: 0; }
  .volume-badge { position: absolute; left: 52px; top: 243px; width: 46px; height: 46px; border-radius: 50%;
    background: var(--wine-red); border: 3px solid var(--paper); display: flex; align-items: center; justify-content: center;
    font-family: "Oswald", sans-serif; font-size: 12px; }
  .bottle-equivalent { position: absolute; left: 17px; top: 265px; display: flex; align-items: center; gap: 6px; }
  .bottle-equivalent .volume { position: static; font-size: 15px; }

  .top-flap-brand { position: absolute; left: 647px; top: 88px; width: 250px; height: 77px; transform: rotate(180deg); }
  .top-flap-brand .brand-name { left: 20px; top: 28px; font-size: 22px; }
  .top-flap-brand .tagline { left: 22px; top: 54px; font-size: 12px; }

  .signature-lockup { position: absolute; left: 58px; top: 858px; }
  .signature-lockup .brand-name { position: static; display: flex; align-items: center; gap: 8px; font-size: 44px; }
  .signature-lockup .square { width: 14px; height: 14px; background: var(--wine-red); }
  .signature-lockup .tagline { position: static; display: block; font-size: 24px; margin-top: 8px; }
</style>
</head>
<body>

<svg class="dieline-lines" width="1200" height="1000" viewBox="0 0 1200 1000" aria-hidden="true">
  <!-- glue flap -->
  <path d="M97 165 H72 L60 178 V472 L72 485 H97" fill="var(--paper)" stroke="var(--line)"/>
  <!-- outlined top flaps with handle cut -->
  <path d="M97 165 V62 Q97 40 120 40 H225 Q247 40 247 62 V165" fill="var(--paper)" stroke="var(--line)"/>
  <rect x="193" y="66" width="34" height="16" rx="8" transform="rotate(-35 210 74)" fill="none" stroke="var(--line)"/>
  <path d="M497 165 V62 Q497 40 520 40 H625 Q647 40 647 62 V165" fill="var(--paper)" stroke="var(--line)"/>
  <rect x="593" y="66" width="34" height="16" rx="8" transform="rotate(-35 610 74)" fill="none" stroke="var(--line)"/>
  <!-- dark top flaps -->
  <path d="M247 165 V98 Q247 88 257 88 H487 Q497 88 497 98 V165 Z" fill="var(--ink)" stroke="var(--line)"/>
  <rect x="300" y="124" width="28" height="13" rx="6.5" transform="rotate(35 314 130)" fill="none" stroke="#777"/>
  <path d="M647 165 V98 Q647 88 657 88 H887 Q897 88 897 98 V165 Z" fill="var(--ink)" stroke="var(--line)"/>
  <rect x="700" y="124" width="28" height="13" rx="6.5" transform="rotate(35 714 130)" fill="none" stroke="#777"/>
  <!-- bottom flaps -->
  <rect x="97" y="485" width="150" height="127" fill="var(--ink)"/>
  <path d="M107 485 Q102 540 140 560 Q175 575 200 560 Q240 540 237 485" fill="none" stroke="#666"/>
  <path d="M247 485 V545 Q247 555 257 555 H487 Q497 555 497 545 V485" fill="var(--ink)" stroke="#666"/>
  <rect x="497" y="485" width="150" height="127" fill="var(--ink)"/>
  <path d="M507 485 Q502 540 540 560 Q575 575 600 560 Q640 540 637 485" fill="none" stroke="#666"/>
  <path d="M647 485 V545 Q647 555 657 555 H887 Q897 555 897 545 V485" fill="var(--ink)" stroke="#666"/>
</svg>

<div class="top-flap-brand">
  <span class="brand-name">TAVIN</span>
  <span class="tagline">California Red Wine</span>
</div>

<section class="panel panel--side-a">
  <span class="brand-name side-brand">TAVIN</span>
  <span class="tagline side-tagline">California Red Wine</span>
  <p class="small-print" style="top:104px">Product of USA,<br>CALIFORNIA<br>Napa Valley / Sonoma county</p>
  <div class="map-area" role="img" aria-label="Map of California wine counties"></div>
  <svg class="glass-outline" width="150" height="320" aria-hidden="true">
    <path d="M42 190 H110 V235 L96 250 H56 L42 235 Z" fill="none" stroke="#bbb" stroke-width="1"/>
  </svg>
  <div class="volume-badge">3.0 L</div>
  <p class="abv" style="top:297px">12,0 % vol.</p>
</section>

<section class="panel panel--front">
  <div class="panel__white-half"></div>
  <div class="origin-tag">Product of U.S.A.</div>
  <span class="brand-name front-brand">TAVIN</span>
  <span class="tagline front-tagline">California Wine</span>
  <div class="art-panther" role="img" aria-label="Black panther illustration crouching forward with red script 'Red' and wine splash"></div>
  <span class="volume front-volume">3.0 L</span>
</section>

<section class="panel panel--side-b">
  <span class="brand-name side-brand">TAVIN</span>
  <span class="tagline side-tagline">California Red Wine</span>
  <p class="small-print" style="top:188px">Product of USA,<br>CALIFORNIA<br>Napa Valley / Sonoma county</p>
  <div class="bottle-equivalent">
    <span class="volume">3.0 L =</span>
    <svg width="40" height="26" viewBox="0 0 40 26" aria-label="Equals four bottles">
      <g fill="var(--deep-red)">
        <path d="M2 26 V10 Q2 7 4 6 V0 H6 V6 Q8 7 8 10 V26 Z"/>
        <path d="M12 26 V10 Q12 7 14 6 V0 H16 V6 Q18 7 18 10 V26 Z"/>
        <path d="M22 26 V10 Q22 7 24 6 V0 H26 V6 Q28 7 28 10 V26 Z"/>
        <path d="M32 26 V10 Q32 7 34 6 V0 H36 V6 Q38 7 38 10 V26 Z"/>
      </g>
    </svg>
  </div>
  <p class="abv" style="top:296px; text-align:left; padding-left:17px">12,0 % vol.</p>
</section>

<section class="panel panel--back">
  <div class="panel__white-half"></div>
  <div class="origin-tag">Product of U.S.A.</div>
  <span class="brand-name front-brand">TAVIN</span>
  <span class="tagline front-tagline">California Wine</span>
  <div class="art-panther" role="img" aria-label="Black panther illustration crouching forward"></div>
  <span class="volume front-volume">3.0 L</span>
</section>

<div class="signature-lockup">
  <span class="brand-name">TAVIN <span class="square"></span></span>
  <span class="tagline">California Red Wine</span>
</div>

</body>
</html>
```